Gift voucher for a photo shoot, folding card DIN long (21 x 9.8 cm)

Hello, I'm a professional photographer and need a new design for my gift voucher card for a photo shoot. The design should be applicable to all types of photo shoots (neutral). I prefer a sophisticated design. The folded card should be printed on both sides.
My data should be included: Logo, Address: Wendtholzer Strße 27, 07549 Gera, Email: fotograf@malteburgardt.eu, Website: www.malteburgardt.eu Tel.: 0173 / 4958302
Updates

Please design the folding card in DIN long format (105 x 210 mm, landscape format). The card should open horizontally. Please design the front with the words "Gift voucher for you" and my logo. Please make the logo small – the words "Gift voucher" should be in the foreground.
The colors - use elegant gray with gold or white font color.
The inside should contain the words: Photo shoot for ........ worth .....€, as well as my logo.
My contact details should be on the back.

Target Market(s)

Private customer

Colors

Designer to choose only greyscale colors for use in the design.

Requirements
Must have
• Noble appearance, a gift voucher that one likes to give away, words: Gift voucher for you, photo shoot for ..., worth .......€
Nice to have
• Noble appearance of the gift voucher, a gift voucher that you like to give away
Should not have
• no pictures

```html
<!DOCTYPE html>
<html lang="en">
<head>
<meta charset="utf-8">
<title>Gift Voucher – Malte Burgardt</title>
<link href="https://fonts.googleapis.com/css2?family=Cinzel:wght@500;600&family=Montserrat:wght@400;500&display=swap" rel="stylesheet">
<style>
  :root {
    --backdrop: #ababab;
    --card-dark: #040507;
    --card-light: #ffffff;
    --ink-white: #ffffff;
    --ink-grey: #a3a3a6;
    --ink-dark: #222222;
    --gold: linear-gradient(90deg, #b5832b 0%, #8a5a22 14%, #d4a640 30%, #f5e4a0 44%, #c9982f 58%, #7d4f1f 74%, #d7a640 88%, #8d5d24 100%);
    --shadow: 0 22px 30px -14px rgba(0,0,0,0.45);
  }
  * { margin: 0; padding: 0; box-sizing: border-box; }
  html, body { width: 1200px; height: 1200px; overflow: hidden; background: var(--backdrop); }
  .canvas { position: relative; width: 1200px; height: 1200px; }

  .card { position: absolute; left: 96px; width: 1005px; height: 263px; box-shadow: var(--shadow); overflow: hidden; }
  .card--outside { top: 294px; background: var(--card-dark); }
  .card--inside { top: 623px; background: var(--card-light); }
  .card--outside .fold { position: absolute; left: 504px; top: 0; width: 60px; height: 100%;
    background: linear-gradient(90deg, rgba(255,255,255,0.05), rgba(255,255,255,0)); }
  .card--inside .fold { position: absolute; left: 504px; top: 0; width: 40px; height: 100%;
    background: linear-gradient(90deg, rgba(0,0,0,0.035), rgba(0,0,0,0)); }

  .gold-text { background: var(--gold); -webkit-background-clip: text; background-clip: text; color: transparent; }

  /* back panel: contact */
  .contact { position: absolute; left: 155px; top: 166px; width: 200px; text-align: center;
    font-family: "Montserrat", sans-serif; color: var(--ink-white); font-size: 8.6px; line-height: 16.5px; }
  .contact-icons { display: flex; justify-content: center; align-items: center; gap: 7px; margin-bottom: 4px; }
  .contact-icons svg { width: 9px; height: 9px; }
  .contact-icons .divider { width: 1px; height: 9px; background: #c9982f; }

  /* front panel */
  .brand { position: absolute; left: 506px; width: 490px; top: 18px; text-align: center; }
  .brand-mark { display: block; margin: 0 auto 8px; width: 44px; height: 44px; border: 1.5px solid var(--ink-white); border-radius: 50%; }
  .brand-name { font-family: "Cinzel", serif; font-weight: 500; font-size: 20px; color: var(--ink-white); letter-spacing: 0.5px; }
  .front-title { position: absolute; left: 506px; width: 490px; top: 170px; text-align: center;
    font-family: "Cinzel", serif; font-weight: 600; font-size: 50px; line-height: 1; white-space: nowrap; }
  .front-sub { position: absolute; left: 506px; width: 490px; top: 226px; text-align: center;
    font-family: "Montserrat", sans-serif; font-size: 25px; letter-spacing: 4px; color: var(--ink-grey); line-height: 1; }

  /* inside */
  .backdrop-ring { position: absolute; left: 370px; top: 1px; width: 262px; height: 262px; border: 9px solid #f4f4f4; border-radius: 50%; }
  .inside-title { position: absolute; left: 86px; width: 333px; top: 44px; text-align: center;
    font-family: "Cinzel", serif; font-weight: 600; font-size: 44px; line-height: 1; white-space: nowrap; }
  .inside-for { position: absolute; left: 86px; width: 333px; top: 95px; text-align: center;
    font-family: "Montserrat", sans-serif; font-size: 23px; letter-spacing: 3px; color: var(--ink-grey); line-height: 1; }
  .fill-line { position: absolute; top: 208px; height: 2px;
    background-image: radial-gradient(circle, var(--ink-dark) 0.8px, transparent 1px); background-size: 5.2px 2px; }
  .fill-line--name { left: 64px; width: 382px; }
  .fill-line--value { left: 604px; width: 235px; }
  .worth { position: absolute; left: 624px; top: 56px; width: 262px; height: 24px; }
  .worth-label { position: absolute; left: 0; width: 262px; text-align: center;
    font-family: "Montserrat", sans-serif; font-size: 23px; letter-spacing: 3.5px; color: var(--ink-grey); line-height: 24px; }
  .worth-rule { position: absolute; top: 10px; width: 63px; height: 4px; }
  .worth-rule--left { left: 0; }
  .worth-rule--right { right: 0; }
  .currency { position: absolute; left: 834px; top: 118px; font-family: "Cinzel", serif; font-weight: 600; font-size: 100px; line-height: 1; }
</style>
</head>
<body>
<div class="canvas">

  <section class="card card--outside" aria-label="Outside of folded card">
    <div class="fold"></div>
    <div class="contact">
      <div class="contact-icons">
        <svg viewBox="0 0 10 10" aria-label="phone"><path d="M2 1 L3.5 1 L4.3 3 L3.3 3.8 Q4.2 5.8 6.2 6.7 L7 5.7 L9 6.5 L9 8 Q8.6 9 7.5 9 Q1 8.4 1 2.5 Q1 1.4 2 1 Z" fill="#fff"/></svg>
        <span class="divider"></span>
        <svg viewBox="0 0 10 10" aria-label="website"><circle cx="5" cy="5" r="4" fill="none" stroke="#fff" stroke-width="1"/><ellipse cx="5" cy="5" rx="1.8" ry="4" fill="none" stroke="#fff" stroke-width="0.8"/><path d="M1 5 H9 M1.6 3 H8.4 M1.6 7 H8.4" stroke="#fff" stroke-width="0.7"/></svg>
        <span class="divider"></span>
        <svg viewBox="0 0 10 10" aria-label="email"><rect x="1" y="2.2" width="8" height="5.6" fill="#fff"/><path d="M1 2.2 L5 5.5 L9 2.2" fill="none" stroke="#040507" stroke-width="0.8"/></svg>
        <span class="divider"></span>
        <svg viewBox="0 0 10 10" aria-label="address"><circle cx="5" cy="3.6" r="2.4" fill="none" stroke="#fff" stroke-width="1"/><path d="M5 6 V8 M2 9 H8" stroke="#fff" stroke-width="1"/></svg>
      </div>
      <p>0173 / 4958302</p>
      <p>www.malteburgardt.eu</p>
      <p>fotograf@malteburgardt.eu</p>
      <p>Wendtholzer Strße 27, 07549 Gera</p>
    </div>

    <div class="brand">
      <span class="brand-mark"></span>
      <p class="brand-name">Malte Burgardt</p>
    </div>
    <h1 class="front-title gold-text">Gift Voucher</h1>
    <p class="front-sub">FOR YOU</p>
  </section>

  <section class="card card--inside" aria-label="Inside of folded card">
    <span class="backdrop-ring"></span>
    <div class="fold"></div>
    <h2 class="inside-title gold-text">Photo Shoot</h2>
    <p class="inside-for">FOR</p>
    <span class="fill-line fill-line--name"></span>

    <div class="worth">
      <svg class="worth-rule worth-rule--left" viewBox="0 0 63 4" preserveAspectRatio="none"><polygon points="0,2 63,0 63,4" fill="#a3a3a6"/></svg>
      <span class="worth-label">WORTH</span>
      <svg class="worth-rule worth-rule--right" viewBox="0 0 63 4" preserveAspectRatio="none"><polygon points="0,0 63,2 0,4" fill="#a3a3a6"/></svg>
    </div>
    <span class="fill-line fill-line--value"></span>
    <span class="currency gold-text">€</span>
  </section>

</div>
</body>
</html>
```